Flyer Tally Your Ledger Free

Hi
Can you please design me a DL Flyer for: Tally Your Ledger Free
Info:
Starting a new Business ?
Want to save on bookkeeping fees for your existing business?

You can now save 1000's off bookkeeping fees by Doing it Yourself.

Using our Bookkeeper software you simply key in the information as you go.

We offer one on one training, backup and support.
We can assist you with BAS Preparation and Payrol Advice.

Add Modules as required:
Point of Sale Module
Jobs Management Module
Website Intergration Module

Fee set up assistance and training.

Lets get the ball rolling: 1300 642 815
www.tylfr.com.au
admin@tylfr.com.au (use the logo thing you made)

Target Market(s)

Small Business

Colors
ec1f27
f04a50
f59296
fcdcdc
ffffff

Requirements
Nice to have
• image/s related to bookkeeping

```html
<!DOCTYPE html>
<html lang="en">
<head>
<meta charset="utf-8">
<title>Tally Your Ledger Free – DL Flyer</title>
<link rel="stylesheet" href="https://fonts.googleapis.com/css2?family=Montserrat:wght@500;600;700;800&family=Lato:ital,wght@0,300;0,400;0,700;1,400&display=swap">
<style>
  :root{
    --red:#ec1f27;
    --red-dark:#c8141b;
    --red-soft:#f04a50;
    --pink:#f59296;
    --blush:#fcdcdc;
    --white:#ffffff;
    --ink:#1d1d1d;
    --grey:#6b6767;
    --grey-band:#5f5d5d;
    --stage:#363435;
    --cream:#fff3d6;
  }
  *{box-sizing:border-box;margin:0;padding:0}
  html,body{width:1200px;height:1200px;overflow:hidden;background:var(--stage)}
  .canvas{position:relative;width:1200px;height:1200px;background:var(--stage)}
  .panel{position:absolute;background:var(--white);overflow:hidden;box-shadow:0 4px 14px rgba(0,0,0,.35)}
  .panel-front{left:117px;top:152px;width:440px;height:904px}
  .panel-back{left:642px;top:150px;width:446px;height:916px}
  .panel-art{position:absolute;inset:0}
  .abs{position:absolute}

  /* front */
  .brand{left:0;top:38px;width:440px;display:flex;flex-direction:column;align-items:center}
  .brand-row{display:flex;align-items:center;gap:10px}
  .brand-dot{width:22px;height:22px;border-radius:50%;background:var(--red)}
  .brand-name{font-family:'Montserrat',sans-serif;font-weight:700;font-size:27px;color:var(--red);letter-spacing:-.3px}
  .brand-tagline{margin-top:6px;font-family:'Lato',sans-serif;font-style:italic;font-size:14px;color:var(--grey)}
  .front-title{left:23px;top:432px;color:var(--white);font-family:'Montserrat',sans-serif;line-height:1}
  .front-title .lead{display:block;font-weight:600;font-size:29px}
  .front-title .big{display:block;font-weight:800;font-size:40px;margin-top:6px}
  .question{left:24px;color:var(--white);font-family:'Montserrat',sans-serif;font-weight:700}
  .q-start{top:536px;font-size:16px;letter-spacing:.5px}
  .q-save{top:574px;font-size:19px;line-height:21px;width:400px}
  .q-diy{top:630px;font-size:13.5px;line-height:18px;width:400px}
  .badge{display:flex;flex-direction:column;align-items:center;justify-content:center;text-align:center;border-radius:50%;background:var(--white);border:4px solid var(--red);font-family:'Montserrat',sans-serif;font-weight:700;color:var(--grey)}
  .badge-front{left:25px;top:684px;width:116px;height:116px;font-size:14px;line-height:18px}
  .contact{width:100%;text-align:center;font-family:'Lato',sans-serif}
  .front-call{left:0;top:822px;font-size:18px;color:var(--red)}
  .front-mail{left:0;top:850px;font-size:18px;color:var(--ink)}

  /* back */
  .back-head{left:0;top:30px;width:446px;text-align:center;font-family:'Montserrat',sans-serif;font-weight:700;font-size:20.5px;line-height:27px;color:var(--red)}
  .back-rule{left:116px;top:124px;width:202px;height:2px;background:var(--red);border-radius:2px}
  .ticks{left:26px;top:150px;width:400px;list-style:none;font-family:'Lato',sans-serif;font-size:17.5px;line-height:22px;color:var(--ink)}
  .ticks li{display:flex;gap:10px;margin-bottom:5px}
  .ticks svg{flex:none;margin-top:1px}
  .badge-back{left:35px;top:267px;width:166px;height:166px;border-width:5px;font-size:21px;line-height:25px;letter-spacing:.6px}
  .modules-head{left:28px;top:557px;font-family:'Montserrat',sans-serif;font-weight:600;font-size:26px;color:var(--white)}
  .modules{left:38px;top:602px;list-style:none;font-family:'Lato',sans-serif;font-weight:400;font-size:21px;color:var(--white)}
  .modules li{display:flex;align-items:center;gap:18px;height:49.5px}
  .mod-icon{width:40px;height:40px;border-radius:50%;background:var(--white);display:flex;align-items:center;justify-content:center;flex:none}
  .fee-band{left:0;top:761px;width:446px;height:57px;background:var(--grey-band);color:var(--white);font-family:'Lato',sans-serif;font-weight:700;font-size:20.5px;line-height:57px;padding-left:28px}
  .back-call{left:0;top:836px;font-size:18px;font-weight:700;color:var(--cream)}
  .back-mail{left:0;top:866px;font-size:18px;color:var(--white)}
</style>
</head>
<body>
<main class="canvas">

  <!-- FRONT SIDE -->
  <section class="panel panel-front">
    <svg class="panel-art" width="440" height="904" viewBox="0 0 440 904" aria-hidden="false">
      <defs>
        <linearGradient id="coffeeTone" x1="0" y1="0" x2="1" y2="1">
          <stop offset="0" stop-color="#f3f1ee"/>
          <stop offset=".55" stop-color="#d9d3cc"/>
          <stop offset="1" stop-color="#8c5a3e"/>
        </linearGradient>
        <linearGradient id="redFront" x1="0" y1="0" x2="0" y2="1">
          <stop offset="0" stop-color="#ef2a30"/>
          <stop offset="1" stop-color="#d8161d"/>
        </linearGradient>
      </defs>
      <rect x="0" y="140" width="440" height="380" fill="url(#coffeeTone)" role="img" aria-label="Photo of a person holding a coffee cup while writing in a notebook"/>
      <path d="M0 560 L0 410 C40 380 90 360 150 380 C210 400 230 460 280 470 C340 480 400 440 440 400 L440 560 Z" fill="#6d6a69"/>
      <path d="M0 760 L0 412 C40 385 95 368 150 388 C210 410 230 470 285 480 C345 490 400 460 440 432 L440 740 C380 730 250 750 160 752 C90 754 40 752 0 760 Z" fill="url(#redFront)"/>
      <path d="M0 760 C40 752 90 754 160 752 C250 750 380 730 440 718 L440 740 C380 745 250 760 160 762 C90 764 40 764 0 770 Z" fill="#6d6a69"/>
      <circle cx="200" cy="742" r="47" fill="#ffffff"/>
      <circle cx="200" cy="742" r="43" fill="#c9d8e6" stroke="var(--red)" stroke-width="3" role="img" aria-label="Illustration of two people reading books"/>
    </svg>

    <div class="abs brand">
      <div class="brand-row"><span class="brand-dot"></span><span class="brand-name">Tally Your Ledger Free</span></div>
      <div class="brand-tagline">It's easy enough to do yourself</div>
    </div>

    <h1 class="abs front-title"><span class="lead">Tally Your Ledger</span><span class="big">Free</span></h1>
    <p class="abs question q-start">STARTING A NEW BUSINESS ?</p>
    <p class="abs question q-save">Want to SAVE on bookkeeping fees for your existing business?</p>
    <p class="abs question q-diy">You can now save 1000's off bookkeeping fees by Doing it Yourself.</p>

    <div class="abs badge badge-front">SAVE<br>1000'S OFF<br>Bookkeeping<br>Fees</div>

    <p class="abs contact front-call">Lets get the ball rolling : 1300 642 815</p>
    <p class="abs contact front-mail">admin@tylfr.com.au &nbsp;|&nbsp; www.tylfr.com.au</p>
  </section>

  <!-- BACK SIDE -->
  <section class="panel panel-back">
    <svg class="panel-art" width="446" height="916" viewBox="0 0 446 916">
      <defs>
        <linearGradient id="haze" x1="0" y1="0" x2="0" y2="1">
          <stop offset="0" stop-color="#ffffff"/>
          <stop offset="1" stop-color="#d9d6d4"/>
        </linearGradient>
        <linearGradient id="redBack" x1="0" y1="0" x2="0" y2="1">
          <stop offset="0" stop-color="#ea1e26"/>
          <stop offset="1" stop-color="#d3151c"/>
        </linearGradient>
        <radialGradient id="bookTone" cx=".5" cy=".5" r=".6">
          <stop offset="0" stop-color="#d9c3a0"/>
          <stop offset=".7" stop-color="#8a6a45"/>
          <stop offset="1" stop-color="#3d2a1c"/>
        </radialGradient>
      </defs>
      <rect x="0" y="290" width="446" height="200" fill="url(#haze)" role="img" aria-label="Faded photo of an open book"/>
      <path d="M0 480 L0 466 C120 450 240 460 330 430 C380 415 420 405 446 395 L446 412 C400 430 360 450 300 460 C200 476 100 470 0 480 Z" fill="#6d6a69"/>
      <path d="M0 916 L0 480 C100 470 200 476 300 460 C360 450 400 430 446 412 L446 916 Z" fill="url(#redBack)"/>
      <circle cx="318" cy="446" r="108" fill="var(--red)"/>
      <circle cx="318" cy="446" r="99" fill="#ffffff"/>
      <circle cx="318" cy="446" r="94" fill="url(#bookTone)" role="img" aria-label="Photo of reading glasses resting on an open book"/>
    </svg>

    <h2 class="abs back-head">Using our BOOKKEEPER<br>SOFTWARE you simply key in the<br>information as you go.</h2>
    <div class="abs back-rule"></div>

    <ul class="abs ticks">
      <li><svg width="22" height="22" viewBox="0 0 22 22"><circle cx="11" cy="11" r="9.5" fill="none" stroke="var(--red)" stroke-width="1.5"/><path d="M6.5 11.2 L9.7 14.2 L15.5 7.8" fill="none" stroke="var(--red)" stroke-width="1.8" stroke-linecap="round" stroke-linejoin="round"/></svg><span>We offer one on one training, backup and support.</span></li>
      <li><svg width="22" height="22" viewBox="0 0 22 22"><circle cx="11" cy="11" r="9.5" fill="none" stroke="var(--red)" stroke-width="1.5"/><path d="M6.5 11.2 L9.7 14.2 L15.5 7.8" fill="none" stroke="var(--red)" stroke-width="1.8" stroke-linecap="round" stroke-linejoin="round"/></svg><span>We can assist you with BAS Preparation and Payrol Advice.</span></li>
    </ul>

    <div class="abs badge badge-back">SAVE<br>1000'S OFF<br>Bookkeeping<br>Fees</div>

    <h3 class="abs modules-head">Add Modules as required :</h3>
    <ul class="abs modules">
      <li><span class="mod-icon"><svg width="24" height="24" viewBox="0 0 24 24"><path d="M4 12 L12 4 H20 V12 L12 20 Z" fill="none" stroke="var(--red)" stroke-width="1.6" stroke-linejoin="round"/><circle cx="16" cy="8" r="1.6" fill="var(--red)"/></svg></span>Point of Sale Module</li>
      <li><span class="mod-icon"><svg width="24" height="24" viewBox="0 0 24 24"><path d="M8 3 L5 21 M16 3 L19 21 M7 8 H17 M6.3 13 H17.7 M5.6 18 H18.4" fill="none" stroke="#c98a12" stroke-width="1.8" stroke-linecap="round"/></svg></span>Jobs Management Module</li>
      <li><span class="mod-icon"><svg width="26" height="26" viewBox="0 0 26 26"><g fill="none" stroke="#222" stroke-width="1.5"><circle cx="13" cy="13" r="10"/><ellipse cx="13" cy="13" rx="4.5" ry="10"/><path d="M3 13 H23 M5 8 H21 M5 18 H21"/></g></svg></span>Website Intergration Module</li>
    </ul>

    <div class="abs fee-band">FEE SET UP ASSISTANCE AND TRAINING.</div>

    <p class="abs contact back-call">Lets get the ball rolling : 1300 642 815</p>
    <p class="abs contact back-mail">admin@tylfr.com.au &nbsp;|&nbsp; www.tylfr.com.au</p>
  </section>

</main>
</body>
</html>
```